Design for Chirpwall Ad to promote Laptops purchase

Need a graphic design for a Chirpwall Ad - to promote 2 laptops (PC and Zorvane) with the stated required ad-text.

AD TEXT:

FOR SME BUSINESS ONLY!
Chat with us!
To get advice on how to apply
and defray up to 80%* of business laptop purchase cost!

*Terms and Conditions apply

Image for reference only

Target Market(s)

Small medium business

Font styles to use
Sans Serif

Requirements
Must have
• 2 laptop images (see attached ) - 1 vector image of ZORVANE , and pls try to create another vector image of PC laptop (where screen is showing Blue Pendrel screen)

```html
<!DOCTYPE html>
<html lang="en">
<head>
<meta charset="utf-8">
<title>SME Laptop Ad</title>
<link rel="stylesheet" href="https://fonts.googleapis.com/css2?family=Raleway:wght@700;800&family=Nunito:wght@400;600;900&family=Arimo&display=swap">
<style>
  :root {
    --purple: #5b12cc;
    --violet: #9e24a6;
    --royal: #1f3ee0;
    --text-blue: #1530e0;
    --silver: #c9c9cc;
    --bubble-start: #4a70c8;
    --bubble-end: #c6c6c8;
    --ink: #1a1a1a;
    --paper: #ffffff;
  }
  html, body {
    margin: 0;
    padding: 0;
    width: 1200px;
    height: 1200px;
    overflow: hidden;
    background: var(--paper);
  }
  .ad {
    position: relative;
    width: 1200px;
    height: 1200px;
    background: var(--paper);
  }
  .ad-art {
    position: absolute;
    inset: 0;
    width: 1200px;
    height: 1200px;
  }
  .headline {
    font-family: "Raleway", sans-serif;
    font-weight: 800;
    font-size: 73px;
    fill: var(--violet);
  }
  .bubble-copy {
    font-family: "Nunito", sans-serif;
    fill: var(--text-blue);
  }
  .bubble-copy--lead { font-weight: 400; font-size: 29px; }
  .bubble-copy--offer { font-weight: 900; font-size: 37px; letter-spacing: 0.5px; }
  .audience {
    position: absolute;
    left: 108px;
    top: 855px;
    margin: 0;
    font-family: "Raleway", sans-serif;
    font-weight: 700;
    font-size: 56px;
    line-height: 64px;
    color: var(--violet);
  }
  .fine-print {
    position: absolute;
    left: 44px;
    top: 1114px;
    margin: 0;
    font-family: "Arimo", sans-serif;
    font-size: 20px;
    line-height: 30px;
    color: var(--ink);
  }
</style>
</head>
<body>
<main class="ad">
  <svg class="ad-art" viewBox="0 0 1200 1200" xmlns="http://www.w3.org/2000/svg">
    <defs>
      <linearGradient id="bubble-stroke" x1="0" y1="0" x2="1" y2="1">
        <stop offset="0" stop-color="var(--bubble-start)"/>
        <stop offset="0.55" stop-color="var(--bubble-end)"/>
      </linearGradient>
      <linearGradient id="zorvane-tones" x1="0" y1="0" x2="0" y2="1">
        <stop offset="0" stop-color="#e9d3ee"/>
        <stop offset="1" stop-color="#e2e2e6"/>
      </linearGradient>
      <linearGradient id="pc-tones" x1="0" y1="0" x2="0" y2="1">
        <stop offset="0" stop-color="#cfe6f8"/>
        <stop offset="1" stop-color="#e4e4e7"/>
      </linearGradient>
    </defs>

    <g class="corner-bands corner-bands--top">
      <polygon points="0,130 0,285 190,107 330,64" fill="var(--silver)"/>
      <polygon points="0,163 0,215 190,107" fill="var(--royal)"/>
      <polygon points="0,0 845,0 0,103" fill="var(--purple)"/>
    </g>

    <g class="corner-bands corner-bands--bottom">
      <polygon points="1200,912 1200,1062 860,1133 1007,1092" fill="var(--silver)"/>
      <polygon points="1200,983 1200,1040 1007,1092" fill="var(--royal)"/>
      <polygon points="342,1200 1200,1097 1200,1200" fill="var(--purple)"/>
    </g>

    <rect class="product product--zorvane" role="img"
      aria-label="Photo of a silver Zorvane laptop, open, with a purple and pink galaxy wallpaper"
      x="107" y="520" width="525" height="264" rx="14" fill="url(#zorvane-tones)"/>
    <rect class="product product--pc" role="img"
      aria-label="Photo of a silver PC laptop, open, showing a blue Pendrel start screen"
      x="648" y="561" width="480" height="370" rx="14" fill="url(#pc-tones)"/>

    <path class="speech-bubble"
      d="M 500 520
         C 430 470 404 400 404 328
         C 404 194 532 86 689 86
         C 846 86 974 194 974 328
         C 974 462 846 570 689 570
         C 640 570 600 562 612 556
         L 480 651
         L 512 530 Z"
      fill="var(--paper)" stroke="url(#bubble-stroke)" stroke-width="19" stroke-linejoin="round"/>

    <text class="headline" x="692" y="233" text-anchor="middle">Chat with</text>
    <text class="headline" x="700" y="323" text-anchor="middle">us!</text>
    <text class="bubble-copy bubble-copy--lead" x="693" y="361" text-anchor="middle">To get advice on how to applyand</text>
    <text class="bubble-copy bubble-copy--offer" x="693" y="407" text-anchor="middle">DEFRAY UP TO 80% OF</text>
    <text class="bubble-copy bubble-copy--lead" x="697" y="440" text-anchor="middle">business Laptop purchase cost!</text>
  </svg>

  <h1 class="audience">FOR SME<br>BUSINESS ONLY!</h1>
  <p class="fine-print">Images for reference only.<br>*Terms &amp; Conditions apply</p>
</main>
</body>
</html>
```